Halvorn - Refresh the look and feel of an existing website

We currently have an existing website www.halvornworldadvisory.example however it needs a more refreshed 'look and feel'. We are a professional consultancy that works with large corporate organisations and government. Our 'tag line' is A New Way of Thinking. We want the site to communicate "Innovation" and Leading Edge Thinking.

Target Market(s)

Corporate and Professional Clients - Organisation and Business Change

Industry/Entity Type

Management Consulting

Number of Pages Required

1 page

Font styles to use
Sans Serif

Requirements
Must have
• Must have a professional Corporate look and feel. Header 'imagery' is ok but boxes on front page need changing ... along with the words. The focus on home page needs to 'call out' 3 main consulting areas:-
• - Change & Transformation Specialists
• - Innovative Solutions
• - Digital Transformation
• Tag Line for business is ... A New Way of Thinking (Highlighting Halvorn as 'Thought Leaders' in business)
Nice to have
• Less "words' more imagery. Possibly an area for a 'video' or recent articles/blogs on the front page. Needs to have more of an 'interactive' feel. We are open to suggestions.
Should not have
• NA

```html
<!DOCTYPE html>
<html lang="en">
<head>
<meta charset="utf-8">
<title>Halvorn – A New Way of Thinking</title>
<link rel="stylesheet" href="https://fonts.googleapis.com/css2?family=Open+Sans:ital,wght@0,400;0,600;0,700;1,600;1,700&family=Arimo:wght@400;700&family=Roboto+Condensed:wght@700&display=swap">
<style>
:root{
  --navy:#14254a;
  --slate:#2a4460;
  --band:#565f82;
  --pale:#dde1ee;
  --ink:#1c2540;
  --link:#2b4a86;
  --muted:#555c6c;
  --white:#ffffff;
}
*{margin:0;padding:0;box-sizing:border-box}
html,body{width:996px;height:1200px;overflow:hidden}
body{position:relative;background:var(--pale);font-family:'Arimo',Arial,sans-serif;color:var(--ink)}
.abs{position:absolute}

/* header */
.site-header{left:0;top:0;width:996px;height:60px;background:linear-gradient(#eef0f8,#d9def0);border-bottom:1px solid #b9c1d8}
.brand{left:190px;top:9px;display:flex;align-items:center;gap:8px}
.brand-mark{width:40px;height:40px;border-radius:50%;background:var(--slate)}
.brand-name{font-family:'Open Sans',sans-serif;font-weight:600;font-size:22px;color:var(--slate);letter-spacing:.5px}
.main-nav{left:393px;top:21px;display:flex;gap:24px;font-family:'Open Sans',sans-serif;font-weight:700;font-size:9.5px;color:var(--link);white-space:nowrap}
.main-nav span{padding:3px 0}
.main-nav .current{background:#fff;color:#000;padding:3px 10px;border-radius:10px;box-shadow:0 1px 3px rgba(0,0,0,.35);margin-right:-6px}

/* hero */
.hero-visual{left:0;top:60px;width:996px;height:327px;background:linear-gradient(90deg,#c6c6c2 0%,#dcdcd6 30%,#e9e9e2 60%,#f2f2ea 100%)}
.hero-panel{left:485px;top:149px;width:511px;height:159px;background:var(--slate);color:var(--white);padding:23px 36px}
.hero-panel h1{font-family:'Open Sans',sans-serif;font-weight:600;font-size:24px;line-height:29px}
.hero-panel p{font-family:'Open Sans',sans-serif;font-size:15.5px;line-height:19px;margin-top:14px;color:#e4e8f0;width:345px}

/* call to action */
.cta-text{left:190px;top:421px;font-size:23.5px;line-height:23px;color:var(--ink);white-space:nowrap}
.cta-button{left:597px;top:415px;width:224px;height:62px;border:3px solid #fff;border-radius:5px;background:linear-gradient(#4a56a0,#8a95d6);box-shadow:0 1px 4px rgba(0,0,0,.3);color:#fff;font-family:'Roboto Condensed','Arial Narrow',sans-serif;font-weight:700;white-space:nowrap;overflow:hidden}
.cta-button svg{position:absolute;left:20px;top:20px}
.cta-button .small{position:absolute;left:60px;top:8px;font-size:15px;line-height:16px}
.cta-button .big{position:absolute;left:60px;top:25px;font-size:22px;line-height:24px}
.rule{left:190px;top:505px;width:650px;height:2px;background:linear-gradient(90deg,transparent,#b8c0d6,transparent)}

/* service areas */
.service{top:537px;width:240px}
.service-icon{position:absolute;left:0;top:1px;width:33px;height:33px;border-radius:50%;border:1.5px solid #8d93a8;background:#eef0f6}
.service-icon svg{position:absolute;left:6px;top:6px}
.service h3{position:absolute;left:41px;top:5px;font-family:'Open Sans',sans-serif;font-weight:700;font-size:11.5px;color:var(--ink);white-space:nowrap}
.service p{position:absolute;left:41px;top:28px;width:170px;font-size:8.8px;line-height:12px;color:var(--muted)}
.learn-more{position:absolute;left:39px;top:90px;width:72px;height:16px;border-radius:8px;background:linear-gradient(#fff,#dfe3ee);box-shadow:0 1px 2px rgba(0,0,0,.4);font-family:'Open Sans',sans-serif;font-weight:600;font-size:7.5px;color:var(--link);text-align:center;line-height:16px}

/* about */
.about-band{left:0;top:685px;width:996px;height:227px;background:var(--band)}
.about-tab{left:272px;top:685px;width:448px;height:80px;background:var(--navy);color:#fff;text-align:center;font-family:'Open Sans',sans-serif;font-weight:700;font-size:26px;line-height:76px;letter-spacing:.5px}
.about-tab::after{content:"";position:absolute;left:86px;top:80px;border-left:18px solid transparent;border-right:18px solid transparent;border-top:14px solid var(--navy)}
.stat-divider{top:803px;width:3px;height:97px;background:#fff}
.stat{top:780px;width:178px;text-align:center;color:#fff;font-family:'Open Sans',sans-serif;font-style:italic}
.stat .num{font-weight:700;font-size:35px;line-height:45px}
.stat svg{display:block;margin:2px auto 0;width:40px;height:40px}
.stat .label{font-weight:600;font-size:16.5px;line-height:22px;margin-top:4px}

/* subscribe */
.subscribe-title{left:0;top:948px;width:980px;text-align:center;font-family:'Open Sans',sans-serif;font-weight:600;font-size:25px;color:var(--slate)}
.field{top:1008px;width:224px;height:41px;background:#fff;border:1px solid #9aa0b4;font-family:'Open Sans',sans-serif;font-size:14px;color:#222;padding:0 14px;line-height:39px}
.subscribe-btn{left:624px;top:1008px;width:223px;height:41px;background:var(--navy);color:#fff;font-family:'Open Sans',sans-serif;font-weight:600;font-size:18px;letter-spacing:.5px;line-height:41px;padding-left:50px}
.subscribe-btn svg{position:absolute;left:167px;top:13px}

/* footer */
.site-footer{left:0;top:1122px;width:996px;height:78px;background:var(--band);color:#fff}
.footer-links{left:189px;top:1128px;font-size:9px;color:#fff;white-space:nowrap}
.footer-links span{margin:0 4px}
.social{top:1125px;width:24px;height:24px;border-radius:4px;background:#3f4560;border:1px solid #2d3248}
.social svg{position:absolute;left:3px;top:5px}
.contact{top:1160px;display:flex;align-items:center;gap:10px;font-size:8.5px;color:#fff;line-height:10px;white-space:nowrap}
.map{left:748px;top:1076px;width:248px;height:124px;border:2px solid #3e4663;background:linear-gradient(135deg,#e8ebf2,#d6dbe6 55%,#c9cfdc)}
.map-address{left:752px;top:1166px;width:240px;height:30px;background:rgba(30,30,30,.82);color:#fff;font-family:'Open Sans',sans-serif;font-style:italic;font-size:11px;line-height:12px;padding:3px 6px;white-space:nowrap}
.map-address span{display:block;text-align:right}
</style>
</head>
<body>

<header class="site-header abs"></header>
<div class="brand abs"><div class="brand-mark"></div><div class="brand-name">HALVORN</div></div>
<nav class="main-nav abs">
  <span class="current">Home</span><span>About Us</span><span>Our Services</span><span>Solutions</span><span>What's Happening</span><span>Contact Us</span>
</nav>

<div class="hero-visual abs" role="img" aria-label="Photo of a hand sketching a light bulb bursting with business strategy icons"></div>
<section class="hero-panel abs">
  <h1>We Specialise in working with complex problems</h1>
  <p>Our agility and expertise allow us to arrive at the right solution - quickly.</p>
</section>

<p class="cta-text abs">We can make your online business<br>easy &amp; usable for all walks of people</p>
<div class="cta-button abs">
  <svg width="26" height="18" viewBox="0 0 26 18"><path d="M0 6h14V0l12 9-12 9v-6H0z" fill="#1f2645"/></svg>
  <span class="small">LET'S START</span>
  <span class="big">YOUR WEBSITE</span>
</div>
<div class="rule abs"></div>

<section class="service abs" style="left:169px">
  <div class="service-icon"><svg width="18" height="18" viewBox="0 0 18 18" fill="#4a5374"><circle cx="6" cy="5" r="3"/><circle cx="12" cy="7" r="3"/><path d="M0 16c0-4 3-6 6-6s4 1 5 3H0zM7 18c0-4 2-6 5-6s6 2 6 6z"/></svg></div>
  <h3>Change &amp; Transformation Specialists</h3>
  <p>We support all elements of organisational development. Our programs are leading edge and can be tailored specifically to meet your needs.</p>
  <div class="learn-more">LEARN MORE &gt;</div>
</section>
<section class="service abs" style="left:425px">
  <div class="service-icon"><svg width="18" height="18" viewBox="0 0 18 18" fill="#4a5374"><path d="M9 1a6 6 0 0 0-3.5 10.9V14h7v-2.1A6 6 0 0 0 9 1z"/><rect x="6" y="15" width="6" height="2"/></svg></div>
  <h3>Innovative Solutions</h3>
  <p>We support all elements of organisational development. Our programs are leading edge and can be tailored specifically to meet your needs.</p>
  <div class="learn-more">LEARN MORE &gt;</div>
</section>
<section class="service abs" style="left:650px">
  <div class="service-icon"><svg width="18" height="18" viewBox="0 0 18 18" fill="none" stroke="#4a5374" stroke-width="1.8"><rect x="1" y="3" width="16" height="11" rx="1"/><path d="M5 11l4-4 2 2 3-3"/></svg></div>
  <h3>Digital Transformation</h3>
  <p>We support all elements of organisational development. Our programs are leading edge and can be tailored specifically to meet your needs.</p>
  <div class="learn-more">LEARN MORE &gt;</div>
</section>

<section class="about-band abs"></section>
<h2 class="about-tab abs">ABOUT COMPANY</h2>
<div class="stat-divider abs" style="left:135px"></div>
<div class="stat-divider abs" style="left:313px"></div>
<div class="stat-divider abs" style="left:491px"></div>
<div class="stat-divider abs" style="left:669px"></div>
<div class="stat-divider abs" style="left:846px"></div>

<div class="stat abs" style="left:136px">
  <div class="num">55</div>
  <svg viewBox="0 0 40 40" fill="none" stroke="#fff" stroke-width="3"><circle cx="20" cy="20" r="17"/><circle cx="14" cy="15" r="1.5" fill="#fff"/><circle cx="26" cy="15" r="1.5" fill="#fff"/><path d="M11 23q9 9 18 0"/></svg>
  <div class="label">HAPPY CLIENTS</div>
</div>
<div class="stat abs" style="left:314px">
  <div class="num">55</div>
  <svg viewBox="0 0 40 40" fill="none" stroke="#fff" stroke-width="2.5"><path d="M7 3h20v34H7z"/><path d="M11 10h12M11 16h12M11 22h8M11 28h8"/><path d="M35 12L24 30l-3 2 1-4 11-18z" fill="#fff"/></svg>
  <div class="label">WORK</div>
</div>
<div class="stat abs" style="left:492px">
  <div class="num">55</div>
  <svg viewBox="0 0 42 42"><circle cx="21" cy="21" r="20" fill="#fff"/><path d="M8 14c4-3 8-1 10 2s-2 5 0 8-3 8-6 6-6-8-4-16zM24 8c5 0 9 4 11 9-3 1-6-1-8 2s2 8-2 11c-2-4-5-6-3-11s-3-7 2-11z" fill="var(--band)"/></svg>
  <div class="label">COUNTRIES</div>
</div>
<div class="stat abs" style="left:670px">
  <div class="num">55</div>
  <svg viewBox="0 0 40 40" fill="#fff"><rect x="3" y="28" width="6" height="10"/><rect x="12" y="22" width="6" height="16"/><rect x="21" y="16" width="6" height="22"/><rect x="30" y="10" width="6" height="28"/><path d="M3 22L22 8l4 3 8-8" fill="none" stroke="#fff" stroke-width="3"/><path d="M28 1h9v9z"/></svg>
  <div class="label">YEARS</div>
</div>

<h2 class="subscribe-title abs">Subscribe Now For Our Latest News</h2>
<div class="field abs" style="left:137px">Email</div>
<div class="field abs" style="left:381px">Name</div>
<div class="subscribe-btn abs">SUBSCRIBE<svg width="10" height="16" viewBox="0 0 10 16" fill="none" stroke="#fff" stroke-width="2"><path d="M1 1l7 7-7 7"/></svg></div>

<footer class="site-footer abs"></footer>
<div class="footer-links abs">Home<span>|</span>Services<span>|</span>Portfolio<span>|</span>Testimonial<span>|</span>Blog<span>|</span>Contact Us</div>
<div class="social abs" style="left:578px"></div>
<div class="social abs" style="left:611px"></div>
<div class="social abs" style="left:644px"></div>
<div class="social abs" style="left:677px"><svg width="16" height="12" viewBox="0 0 16 12" fill="none" stroke="#fff" stroke-width="1.4"><rect x="1" y="1" width="14" height="10"/><path d="M1 1l7 6 7-6"/></svg></div>

<div class="contact abs" style="left:63px">
  <svg width="24" height="22" viewBox="0 0 24 22" fill="none" stroke="#fff" stroke-width="1.5"><path d="M2 9l10-7 10 7v12H2z"/><path d="M2 9l10 7 10-7"/></svg>
  <span>info@halvornworldadvisory.example</span>
</div>
<div class="contact abs" style="left:298px">
  <svg width="26" height="26" viewBox="0 0 26 26" fill="none" stroke="#fff" stroke-width="1.5"><circle cx="13" cy="13" r="11"/><ellipse cx="13" cy="13" rx="5" ry="11"/><path d="M2 13h22M4 7h18M4 19h18"/></svg>
  <span>www.halvornworldadvisory.example</span>
</div>
<div class="contact abs" style="left:528px">
  <svg width="20" height="24" viewBox="0 0 20 24" fill="#fff"><path d="M4 1l4 5-2 3c1 3 3 6 6 8l3-2 4 5-3 3C8 22 1 13 1 4z"/></svg>
  <span>In Australia: 1300 555 018<br>From overseas: (+613) 5550 2816</span>
</div>

<div class="map abs" role="img" aria-label="Map of Australia marking the office location"></div>
<div class="map-address abs">PO Box 18 Larkin Street<span>East Victoria 8100 AUSTRALIA</span></div>

</body>
</html>
```